Software engineering company needs business card

I need a cool business card. Company: Soft Belan Brindlewood Ave 41 58207 Ostervale Name: Gerald Vanholt CEO / Managing Director & Owner

```html
<!DOCTYPE html>
<html lang="de">
<head>
<meta charset="utf-8">
<title>Soft Belan – Visitenkarte</title>
<link href="https://fonts.googleapis.com/css2?family=Quicksand:wght@400;500;600;700&display=swap" rel="stylesheet">
<style>
  :root {
    --backdrop: #e8ebed;
    --paper: #f6f7f6;
    --brand-green: #6bb52e;
    --brand-slate: #4e5052;
    --ink-muted: #7a7c7e;
    --pin-line: #f2f2f2;
    --shadow: rgba(0, 0, 0, 0.12);
  }
  * { box-sizing: border-box; margin: 0; padding: 0; }
  html, body {
    width: 1200px;
    height: 800px;
    overflow: hidden;
    background: var(--backdrop);
    font-family: "Quicksand", sans-serif;
  }
  .card-sheet {
    position: relative;
    width: 1200px;
    height: 800px;
  }
  .card {
    position: absolute;
    top: 240px;
    width: 520px;
    height: 320px;
    background: var(--paper);
    box-shadow: 0 6px 22px var(--shadow);
    overflow: hidden;
  }
  .card--back { left: 50px; }
  .card--front { left: 630px; }

  .company-name {
    position: absolute;
    display: flex;
    align-items: center;
    font-weight: 600;
    color: var(--brand-slate);
    white-space: nowrap;
  }
  .company-name__mark {
    display: inline-block;
    background: var(--brand-slate);
  }

  /* Back side */
  .card--back .company-name {
    left: 0; right: 0;
    top: 130px;
    justify-content: center;
    gap: 16px;
    font-size: 44px;
    letter-spacing: 0.5px;
  }
  .card--back .company-name__mark { width: 30px; height: 30px; }

  /* Front side */
  .card--front .company-name {
    top: 28px;
    right: 32px;
    gap: 8px;
    font-size: 21px;
  }
  .card--front .company-name__mark { width: 14px; height: 14px; }

  .holder {
    position: absolute;
    left: 36px;
    top: 84px;
  }
  .holder__name {
    font-size: 19px;
    font-weight: 700;
    color: var(--brand-green);
    line-height: 1.1;
  }
  .holder__role {
    font-size: 9.5px;
    font-weight: 500;
    color: var(--ink-muted);
    margin-top: 3px;
  }
  .brand-band {
    position: absolute;
    left: 0; right: 0;
    top: 148px;
    height: 104px;
    background: var(--brand-green);
  }
  .location-tab {
    position: absolute;
    left: 196px;
    top: 120px;
    width: 128px;
    height: 144px;
  }
  .address {
    position: absolute;
    left: 130px;
    width: 260px;
    top: 272px;
    text-align: center;
    font-size: 11px;
    font-weight: 500;
    line-height: 1.5;
    color: var(--ink-muted);
    font-style: normal;
  }
</style>
</head>
<body>
  <main class="card-sheet">
    <section class="card card--back" aria-label="Kartenrückseite">
      <div class="company-name"><span class="company-name__mark"></span>Soft Belan</div>
    </section>

    <section class="card card--front" aria-label="Kartenvorderseite">
      <div class="company-name"><span class="company-name__mark"></span>Soft Belan</div>

      <div class="holder">
        <p class="holder__name">Gerald Vanholt</p>
        <p class="holder__role">CEO / Geschäftsführer &amp; Inhaber</p>
      </div>

      <div class="brand-band"></div>

      <svg class="location-tab" viewBox="0 0 128 144" aria-hidden="true">
        <path d="M0 0 H128 V132 H74 L64 142 L54 132 H0 Z" fill="var(--brand-slate)"/>
        <path d="M64 40 C52 40 45 49 45 58 C45 70 64 88 64 88 C64 88 83 70 83 58 C83 49 76 40 64 40 Z"
              fill="none" stroke="var(--pin-line)" stroke-width="1.6"/>
        <circle cx="64" cy="57" r="6" fill="none" stroke="var(--pin-line)" stroke-width="1.6"/>
      </svg>

      <address class="address">
        Brindlewood Ave 41<br>
        58207 Ostervale
      </address>
    </section>
  </main>
</body>
</html>
```